Tidewell Works's Facebook Cover Design

I am in need of a social media cover for my company's Facebook account. Please leverage the green logos and color palette attached.

Tidewell Works offers 2 primary services:
1.) Business Automation Services
2.) AI (artificial intelligence integrations)

While a lot of what we do is highly technical, what we deliver is not. In a nutshell, we help our clients to connect their data regardless of what application that data is sitting in. Because we can connect that data, often times we can:

A.) offer more intelligent marketing and help our client increase their revenue.
B.) automate highly repetitive tasks using technology and drive down their costs thus saving them money
C.) help our clients use AI to better serve their customers

You can read a little bit about our company here: https://www.tidewellworks.example

Our tagline is: "Connect data to increase the flow of profitability."

Visually, we'd like your help to illustrate the "connecting" of these applications. Please let me know if you have any questions.

Target Market(s)

Business Owners or Marketing Managers

Industry/Entity Type

Marketing technologies.

Font styles to use
Sans Serif

Requirements
Must have
• Please make every effort to have the cover compatible with the color palette of the attached images.
Should not have
• Please do not use the standard clipart or stock libraries of AI = robot. If you do, please make them small. We help business glue their data from different sources to solve real work problems. Little robots are overused.

```html
<!DOCTYPE html>
<html lang="en">
<head>
<meta charset="utf-8">
<title>Tidewell Works – Facebook Cover</title>
<link href="https://fonts.googleapis.com/css2?family=Barlow:wght@500;600;700&family=Barlow+Semi+Condensed:wght@700;800&display=swap" rel="stylesheet">
<style>
  :root {
    --page-bg: #cbced7;
    --cover-bg: #f5f5f6;
    --panel-light: #ececee;
    --brand-green: #84c450;
    --brand-dark: #4b4b4d;
    --ink: #1c1c1e;
    --photo-top: #a9a6a3;
    --photo-bottom: #3d3d40;
  }
  * { margin: 0; padding: 0; box-sizing: border-box; }
  html, body {
    width: 1200px; height: 1156px; overflow: hidden;
    background: var(--page-bg);
  }
  .stage {
    position: relative; width: 1200px; height: 1156px;
  }
  .cover-frame {
    position: absolute; left: 50px; top: 374px;
    width: 1100px; height: 407px; overflow: hidden;
  }
  .cover {
    position: absolute; left: 0; top: 0;
    width: 1526px; height: 564px;
    transform: scale(0.7208); transform-origin: 0 0;
    background: var(--cover-bg);
    overflow: hidden;
    font-family: "Barlow", sans-serif;
    color: var(--ink);
  }
  .cover-shapes { position: absolute; inset: 0; }
  .portrait {
    position: absolute; left: 154px; top: 25px;
    width: 370px; height: 539px;
    border-radius: 150px 150px 0 0;
    background: linear-gradient(180deg, var(--photo-top) 0%, #6f6c6a 45%, var(--photo-bottom) 100%);
  }
  .brand-name {
    position: absolute; left: 614px; top: 48px;
    font-family: "Barlow", sans-serif; font-weight: 700;
    font-size: 58px; line-height: 1; color: var(--brand-dark);
    letter-spacing: -0.5px;
  }
  .headline {
    position: absolute; left: 610px; top: 146px;
    font-family: "Barlow Semi Condensed", sans-serif; font-weight: 800;
    font-size: 97px; line-height: 1; color: var(--brand-green);
    letter-spacing: 1px;
  }
  .tagline {
    position: absolute; left: 617px; top: 234px;
    font-family: "Barlow Semi Condensed", sans-serif; font-weight: 700;
    font-size: 39px; line-height: 1; color: var(--ink);
    letter-spacing: 0.5px;
  }
  .tagline .accent { color: var(--brand-green); }
  .services-title {
    position: absolute; left: 619px; top: 301px;
    font-family: "Barlow Semi Condensed", sans-serif; font-weight: 700;
    font-size: 42px; line-height: 1; color: var(--ink);
  }
  .service-list {
    position: absolute; left: 620px; top: 352px;
    list-style: none;
  }
  .service-list li {
    display: flex; align-items: center; gap: 14px;
    height: 47px;
    font-size: 29px; font-weight: 600; color: var(--ink);
  }
  .service-list svg { width: 27px; height: 27px; flex: none; }
  .web-pill {
    position: absolute; left: 611px; top: 472px;
    height: 45px; padding: 0 22px 0 16px;
    border-radius: 23px; background: var(--brand-green);
    display: flex; align-items: center; gap: 12px;
    font-size: 29px; font-weight: 500; color: var(--ink);
  }
  .web-pill svg { width: 28px; height: 28px; }
</style>
</head>
<body>
<div class="stage">
  <div class="cover-frame">
    <div class="cover">
      <svg class="cover-shapes" viewBox="0 0 1526 564" width="1526" height="564" aria-hidden="true">
        <polygon points="330,0 620,0 1060,564 770,564" fill="var(--panel-light)"/>
        <polygon points="980,0 1140,0 1526,420 1526,564 1400,564" fill="#efeff1"/>
        <polygon points="460,0 520,0 960,564 900,564" fill="#ffffff" opacity="0.7"/>
        <circle cx="20" cy="-40" r="178" fill="var(--brand-dark)"/>
        <circle cx="230" cy="610" r="337" fill="none" stroke="var(--brand-green)" stroke-width="66"/>
        <circle cx="1524" cy="170" r="70" fill="var(--brand-green)"/>
        <circle cx="1524" cy="615" r="210" fill="none" stroke="var(--brand-dark)" stroke-width="40"/>
      </svg>

      <div class="portrait" role="img" aria-label="Photo of a smiling businessman in a dark blazer holding an open laptop"></div>

      <div class="brand-name">Tidewell Works</div>
      <h1 class="headline">CONNECT DATA</h1>
      <p class="tagline">TO INCREASE THE FLOW OF <span class="accent">PROFITABILITY</span></p>

      <h2 class="services-title">OUR SERVICES</h2>
      <ul class="service-list">
        <li>
          <svg viewBox="0 0 26 26"><circle cx="13" cy="13" r="13" fill="var(--brand-green)"/><path d="M7 13.5l4 4 8-8" fill="none" stroke="#fff" stroke-width="3" stroke-linecap="round" stroke-linejoin="round"/></svg>
          Business Automation Services
        </li>
        <li>
          <svg viewBox="0 0 26 26"><circle cx="13" cy="13" r="13" fill="var(--brand-green)"/><path d="M7 13.5l4 4 8-8" fill="none" stroke="#fff" stroke-width="3" stroke-linecap="round" stroke-linejoin="round"/></svg>
          AI (artificial intelligence integrations)
        </li>
      </ul>

      <div class="web-pill">
        <svg viewBox="0 0 28 28" fill="none" stroke="var(--ink)" stroke-width="2">
          <circle cx="14" cy="14" r="12"/>
          <ellipse cx="14" cy="14" rx="5.5" ry="12"/>
          <line x1="2" y1="14" x2="26" y2="14"/>
          <path d="M4.5 8h19M4.5 20h19"/>
        </svg>
        www.tidewellworks.example
      </div>
    </div>
  </div>
</div>
</body>
</html>
```